Business Card Design

we are a small based family business that specialise in 12v led lights for kelvo caravans.
we also sell 12v switches, wire, circuit breakers, dimmers etc but our main line is LEDs.
We would like something that reflects the LED lighting on our cards.
www.willowtreeleds.com.au is where you can have a look at to get ideas, of our product.
I have attached the logo we generally use on all our tradio listings and is the main header on our website.

Look forward to seeing what your team comes up with.

Industry/Entity Type

Business

Contact Information for Business Card

Tam 0491 738 205
Cedarwood Vale QLD 4312

www.willowtreeleds.com

```html
<!DOCTYPE html>
<html lang="en">
<head>
<meta charset="utf-8">
<title>Willow Tree LEDs – Business Cards</title>
<link href="https://fonts.googleapis.com/css2?family=Exo+2:wght@300;400;600;800&display=swap" rel="stylesheet">
<style>
  :root {
    --page-bg: #e6e6e6;
    --card-white: #ffffff;
    --brand-red: #b3260a;
    --band-black: #0e0e0e;
    --accent-orange: #e8642c;
    --muted-grey: #5a5a5a;
    --row-on-red: rgba(0, 0, 0, 0.18);
    --row-on-black: rgba(255, 255, 255, 0.07);
    --ink-light: #ffffff;
  }
  * { box-sizing: border-box; margin: 0; padding: 0; }
  html, body {
    width: 1200px; height: 1200px; overflow: hidden;
    background: var(--page-bg);
    font-family: "Exo 2", sans-serif;
  }
  .canvas { position: relative; width: 1200px; height: 1200px; }
  .card {
    position: absolute; top: 215px;
    width: 440px; height: 770px;
    background: var(--card-white);
    overflow: hidden;
    box-shadow: 0 6px 18px rgba(0,0,0,0.18);
  }
  .card--back { left: 120px; }
  .card--front { left: 640px; }
  .card__shapes { position: absolute; inset: 0; width: 440px; height: 770px; }
  .wordmark {
    position: absolute; left: 0; width: 100%;
    text-align: center;
    font-weight: 800; font-size: 40px; letter-spacing: 0.5px;
    color: var(--brand-red);
    text-transform: uppercase;
  }
  .card--back .wordmark { top: 170px; }
  .card--front .wordmark { top: 140px; }
  .person {
    position: absolute; right: 48px; top: 220px; text-align: right;
  }
  .person__name {
    font-size: 22px; font-weight: 400; letter-spacing: 2px;
    color: var(--accent-orange); text-transform: uppercase;
  }
  .person__title {
    font-size: 15px; font-weight: 600; letter-spacing: 1.5px;
    color: var(--muted-grey); text-transform: uppercase; margin-top: 2px;
  }
  .contact-row {
    position: absolute; left: 40px; width: 340px;
    display: flex; align-items: center; gap: 14px;
    padding: 8px 12px;
    border-radius: 4px;
    background: var(--row-on-red);
    color: var(--ink-light);
    font-size: 20px; font-weight: 300; letter-spacing: 0.5px;
    white-space: nowrap;
  }
  .contact-row--dark { background: var(--row-on-black); }
  .contact-row__icon {
    flex: 0 0 30px; width: 30px; height: 30px;
    border: 1.5px solid var(--ink-light); border-radius: 3px;
    display: flex; align-items: center; justify-content: center;
  }
  .contact-row__icon svg { width: 18px; height: 18px; }
  .contact-row__mark {
    width: 12px; height: 12px; background: var(--ink-light);
  }
</style>
</head>
<body>
<div class="canvas">

  <!-- Back of card: social rows -->
  <section class="card card--back">
    <svg class="card__shapes" viewBox="0 0 440 770" aria-hidden="true">
      <rect x="0" y="290" width="440" height="480" fill="var(--brand-red)"/>
      <polygon points="0,395 440,420 385,462 440,505 0,482" fill="var(--band-black)"/>
    </svg>
    <div class="wordmark">Willow Tree LEDs</div>

    <div class="contact-row" style="top:325px">
      <span class="contact-row__icon"><span class="contact-row__mark"></span></span>
      <span>circlebook.com/urname</span>
    </div>
    <div class="contact-row contact-row--dark" style="top:420px">
      <span class="contact-row__icon"><span class="contact-row__mark"></span></span>
      <span>chirpline.com/urname</span>
    </div>
    <div class="contact-row" style="top:535px">
      <span class="contact-row__icon"><span class="contact-row__mark"></span></span>
      <span>linkpro.com/urname</span>
    </div>
  </section>

  <!-- Front of card: name and contact details -->
  <section class="card card--front">
    <svg class="card__shapes" viewBox="0 0 440 770" aria-hidden="true">
      <rect x="0" y="310" width="440" height="460" fill="var(--band-black)"/>
      <polygon points="0,545 85,480 440,480 440,770 0,770" fill="var(--brand-red)"/>
    </svg>
    <div class="wordmark">Willow Tree LEDs</div>
    <div class="person">
      <div class="person__name">Tam</div>
      <div class="person__title">General Manager</div>
    </div>

    <div class="contact-row contact-row--dark" style="top:338px">
      <span class="contact-row__icon">
        <svg viewBox="0 0 24 24"><path d="M6 2h4l2 5-3 2a11 11 0 0 0 6 6l2-3 5 2v4a2 2 0 0 1-2 2A18 18 0 0 1 4 4a2 2 0 0 1 2-2z" fill="#fff"/></svg>
      </span>
      <span>0491 738 205</span>
    </div>
    <div class="contact-row contact-row--dark" style="top:405px">
      <span class="contact-row__icon">
        <svg viewBox="0 0 24 24"><rect x="2" y="5" width="20" height="14" fill="none" stroke="#fff" stroke-width="2"/><path d="M2 6l10 7 10-7" fill="none" stroke="#fff" stroke-width="2"/></svg>
      </span>
      <span>tam@willowtreeleds.com</span>
    </div>
    <div class="contact-row" style="top:505px">
      <span class="contact-row__icon">
        <svg viewBox="0 0 24 24"><circle cx="12" cy="12" r="9" fill="none" stroke="#fff" stroke-width="2"/><ellipse cx="12" cy="12" rx="4" ry="9" fill="none" stroke="#fff" stroke-width="1.6"/><path d="M3 12h18" stroke="#fff" stroke-width="1.6"/></svg>
      </span>
      <span>www.willowtreeleds.com</span>
    </div>
    <div class="contact-row" style="top:572px">
      <span class="contact-row__icon">
        <svg viewBox="0 0 24 24"><path d="M12 2a7 7 0 0 0-7 7c0 5 7 13 7 13s7-8 7-13a7 7 0 0 0-7-7z" fill="#fff"/><circle cx="12" cy="9" r="2.5" fill="var(--brand-red)"/></svg>
      </span>
      <span>Cedarwood Vale QLD 4312</span>
    </div>
  </section>

</div>
</body>
</html>
```